Successfully Managing through a Hurricane Training Event

This learning event is specifically for Birch Supply retailers/stores located outside of the US who are seeking guidance and help with how to plan, prepare, manage there business during Hurricane/Tropical Storm season.

----------------------------------------------
Event Title: Successfully Managing Through Hurricane Season

Event Description: Hurricanes and severe tropical storms are some of the most devastating, and costly, natural disasters known to humans. In fact, historically, 40% of small businesses impacted by a natural disaster do not reopen. If your business is vulnerable to these potential catastrophic events, it is important to develop an effective preparedness and mitigation plan, and take prompt action. Doing so will not only increase the safety of your store associates and customers, but it will help you remain in business after a hurricane strikes, improving your community’s ability to recover. This session focuses on:

o In-store preparation functions
o Implementing business continuity operating procedures for protecting and maintaining your business
o Sustaining the capability to provide products to customers
o Building a hurricane-ready optimized assortment of in-demand products, including special merchandising opportunities
o Deploying effective inventory management and system strategies for staying in stock
o Knowing your available contacts and rules of engagement
o Preserving a competitive advantage and reputation
o Optimizing the means by which you leverage your freight forwarding facility

Event is hosted by: Birch Worldwide Partners www.birchworldpartnersco.example

Logistical Details:
• Length: 1 hour
• Date: Friday, August 17, 2018
• Time: 1:00 – 2:00 p.m.

To Register for this Event, Go To: https://www.tolvenork.example/birch18/fall/

Pricing: $ 25 per participant
*Charged to Invoice post-show

Questions? For more information, contact Martin Oakes
+1 555-017-2846
moakes@birchsupply.example

Target Market(s)

Birch Supply International Stores

Industry/Entity Type

Retail

Font styles to use
Serif

Requirements
Must have
• See Word File Attachment
• Use Birch Supply red and black logo colors.
• 1 -Sided brochure
Nice to have
Should not have
• N/A

```html
<!DOCTYPE html>
<html lang="en">
<head>
<meta charset="utf-8">
<title>Successfully Managing Through Hurricane Season</title>
<link href="https://fonts.googleapis.com/css2?family=Fira+Sans+Condensed:ital,wght@0,300;0,400;0,500;0,600;0,700;1,600;1,700&display=swap" rel="stylesheet">
<style>
  :root {
    --red: #e31837;
    --band: #c94a5c;
    --ink: #2f3133;
    --body: #3b3d40;
    --paper: #ffffff;
    --footer: #e9e9ea;
    --link: #1d5ea8;
    --sky-top: #a9bccb;
    --sky-bottom: #d3dde4;
    --sun: #f6dc4f;
    --stage: #d9dadc;
  }
  * { box-sizing: border-box; margin: 0; padding: 0; }
  html, body { width: 1200px; height: 1200px; overflow: hidden; background: var(--stage); }
  body { font-family: "Fira Sans Condensed", "Arial Narrow", sans-serif; color: var(--body); }

  .flyer { position: absolute; left: 134px; top: 0; width: 932px; height: 1200px; background: var(--paper); overflow: hidden; }

  .hero { position: absolute; left: 0; top: 0; width: 932px; height: 359px;
    background: linear-gradient(100deg, var(--sky-top) 0%, var(--sky-bottom) 45%, #9fb1ad 70%, #b9c7cf 100%); }
  .hero-photo { position: absolute; inset: 0; background: radial-gradient(ellipse 45% 60% at 72% 40%, rgba(60,80,70,.45), rgba(60,80,70,0) 70%); }

  .title { position: absolute; left: 62px; top: 0; width: 520px; height: 290px; font-weight: 400; }
  .title span { position: absolute; left: 0; display: block; line-height: 1; white-space: nowrap; }
  .title-lead { top: 37px; font-weight: 300; font-size: 68px; color: var(--ink); letter-spacing: 4px; }
  .title-sub { top: 104px; font-weight: 500; font-size: 30px; color: var(--ink); letter-spacing: 6.5px; }
  .title-main { top: 148px; font-weight: 700; font-size: 74px; color: #fff; letter-spacing: 1.5px; }
  .title-season { top: 214px; font-weight: 700; font-size: 70px; color: #fff; letter-spacing: 30px; }

  .hazard-icons { position: absolute; left: 459px; top: 161px; display: flex; gap: 16px; }
  .hazard-icon { width: 119px; height: 119px; border-radius: 50%; background: var(--sun); border: 3px solid var(--red); }

  .intro { position: absolute; left: 62px; top: 296px; width: 820px; font-size: 23.5px; line-height: 29px; font-weight: 500; color: #fff; text-shadow: 0 1px 2px rgba(0,0,0,.35); white-space: nowrap; }

  .band { position: absolute; left: 0; top: 359px; width: 932px; height: 126px; background: linear-gradient(180deg, #c4465a, var(--band)); }
  .band p { position: absolute; left: 62px; top: 22px; width: 790px; font-size: 16px; line-height: 19.5px; font-weight: 500; color: #fff; }

  .focus { position: absolute; left: 62px; top: 498px; width: 830px; }
  .focus-heading { font-size: 46px; line-height: 1; font-style: italic; font-weight: 600; color: var(--red); }
  .focus-list { list-style: none; margin-top: 12px; }
  .focus-list li { position: relative; padding-left: 29px; font-size: 21.5px; line-height: 25px; font-weight: 500; color: var(--body); margin-bottom: 18px; }
  .focus-list svg { position: absolute; left: 0; top: 3px; width: 20px; height: 19px; }

  .footer { position: absolute; left: 0; top: 957px; width: 932px; height: 180px; background: var(--footer); }
  .col { position: absolute; top: 0; height: 180px; }
  .col-host { left: 0; width: 385px; }
  .col-logistics { left: 385px; width: 273px; background: linear-gradient(90deg, #d9d9da 0%, #eeeeef 12%, #eeeeef 100%); }
  .col-pricing { left: 658px; width: 274px; background: linear-gradient(90deg, #d9d9da 0%, #eeeeef 12%, #eeeeef 100%); }
  .col-label { font-size: 21px; font-weight: 500; color: #222; }

  .col-host .col-label { position: absolute; left: 68px; top: 10px; }
  .host-brand { position: absolute; left: 65px; top: 56px; display: flex; align-items: center; gap: 10px; }
  .host-dot { width: 30px; height: 30px; border-radius: 50%; background: var(--red); flex: none; }
  .host-name { font-size: 24px; font-weight: 600; color: #222; line-height: 1.05; }
  .host-url { position: absolute; left: 64px; top: 125px; font-size: 20.5px; font-weight: 500; color: #222; }

  .col-logistics .col-label { position: absolute; left: 32px; top: 14px; }
  .details { position: absolute; left: 32px; top: 55px; list-style: none; font-size: 16px; line-height: 18px; font-weight: 400; color: #333; }
  .details li::before { content: "•"; margin-right: 5px; }

  .register { position: absolute; left: 417px; top: 123px; width: 500px; z-index: 2; }
  .register-label { font-size: 21.5px; font-weight: 500; color: var(--red); line-height: 1.1; white-space: nowrap; }
  .register-url { font-size: 16px; font-weight: 500; color: var(--link); line-height: 1.3; letter-spacing: .3px; white-space: nowrap; }

  .col-pricing .col-label { position: absolute; left: 27px; top: 18px; }
  .price { position: absolute; left: 27px; top: 52px; font-size: 25px; font-weight: 500; color: #222; line-height: 1; }
  .price-note { position: absolute; left: 27px; top: 79px; font-size: 14px; font-weight: 600; color: #222; }

  .contact-bar { position: absolute; left: 0; top: 1137px; width: 932px; height: 63px; background: var(--red); color: #fff; display: flex; align-items: center; padding-left: 63px; font-size: 17.5px; font-weight: 600; white-space: nowrap; }
  .contact-name { font-style: italic; font-size: 22px; margin: 0 6px 0 5px; }
  .sep { margin: 0 9px; font-weight: 400; }
</style>
</head>
<body>
<main class="flyer">
  <section class="hero">
    <div class="hero-photo" role="img" aria-label="Photograph of palm trees bending in hurricane winds along a stormy, misty shoreline"></div>
    <h1 class="title">
      <span class="title-lead">SUCCESSFULLY</span>
      <span class="title-sub">MANAGING THROUGH</span>
      <span class="title-main">HURRICANE</span>
      <span class="title-season">SEASON</span>
    </h1>
    <div class="hazard-icons">
      <div class="hazard-icon" role="img" aria-label="Illustration of a wave and wind storm symbol"></div>
      <div class="hazard-icon" role="img" aria-label="Illustration of a tornado funnel symbol"></div>
    </div>
    <p class="intro">Hurricanes and severe tropical storms are some of the most devastating,<br>and costly, natural disasters known to humans.</p>
  </section>

  <section class="band">
    <p>In fact, historically, 40% of small businesses impacted by a natural disaster do not reopen. If your business is vulnerable to these potential catastrophic events, it is important to develop an effective preparedness and mitigation plan, and take prompt action. Doing so will not only increase the safety of your store associates and customers, but it will help you remain in business after a hurricane strikes, improving your community’s ability to recover.</p>
  </section>

  <section class="focus">
    <h2 class="focus-heading">This session focuses on:</h2>
    <ul class="focus-list">
      <li><svg viewBox="0 0 20 19"><path d="M0 10 L4 8 L8 13 L18 0 L20 1 L8 18 Z" fill="#e31837"/></svg>In-store preparation functions</li>
      <li><svg viewBox="0 0 20 19"><path d="M0 10 L4 8 L8 13 L18 0 L20 1 L8 18 Z" fill="#e31837"/></svg>Implementing business continuity operating procedures for protecting and maintaining your business</li>
      <li><svg viewBox="0 0 20 19"><path d="M0 10 L4 8 L8 13 L18 0 L20 1 L8 18 Z" fill="#e31837"/></svg>Sustaining the capability to provide products to customers</li>
      <li><svg viewBox="0 0 20 19"><path d="M0 10 L4 8 L8 13 L18 0 L20 1 L8 18 Z" fill="#e31837"/></svg>Building a hurricane-ready optimized assortment of in-demand products, including special merchandising opportunities</li>
      <li><svg viewBox="0 0 20 19"><path d="M0 10 L4 8 L8 13 L18 0 L20 1 L8 18 Z" fill="#e31837"/></svg>Deploying effective inventory management and system strategies for staying in stock</li>
      <li><svg viewBox="0 0 20 19"><path d="M0 10 L4 8 L8 13 L18 0 L20 1 L8 18 Z" fill="#e31837"/></svg>Knowing your available contacts and rules of engagement</li>
      <li><svg viewBox="0 0 20 19"><path d="M0 10 L4 8 L8 13 L18 0 L20 1 L8 18 Z" fill="#e31837"/></svg>Preserving a competitive advantage and reputation</li>
      <li><svg viewBox="0 0 20 19"><path d="M0 10 L4 8 L8 13 L18 0 L20 1 L8 18 Z" fill="#e31837"/></svg>Optimizing the means by which you leverage your freight forwarding facility</li>
    </ul>
  </section>

  <section class="footer">
    <div class="col col-host">
      <h3 class="col-label">Event is hosted by:</h3>
      <div class="host-brand">
        <span class="host-dot"></span>
        <span class="host-name">Birch Worldwide Partners</span>
      </div>
      <p class="host-url">www.birchworldpartnersco.example</p>
    </div>
    <div class="col col-logistics">
      <h3 class="col-label">Logistical Details:</h3>
      <ul class="details">
        <li>Length: 1 hour</li>
        <li>Date: Friday, August 17, 2018</li>
        <li>Time: 1:00 – 2:00 p.m.</li>
      </ul>
    </div>
    <div class="col col-pricing">
      <h3 class="col-label">Pricing:</h3>
      <p class="price">$25 per participant</p>
      <p class="price-note">*Charged to Invoice post-show</p>
    </div>
    <div class="register">
      <p class="register-label">To Register for this Event, Go To:</p>
      <p class="register-url">https://www.tolvenork.example/birch18/fall/</p>
    </div>
  </section>

  <footer class="contact-bar">
    Questions? For more information, contact <span class="contact-name">Martin Oakes</span><span class="sep">|</span>+1 555-017-2846<span class="sep">|</span>moakes@birchsupply.example
  </footer>
</main>
</body>
</html>
```